Design a Future- POV MOTSAVIN

Refresh the images/Theme. Focus theme/images on the following

1. Adaptability
2. Resilience
3. Emotional Inteligence
4. Relentless execution
5. High Care Factor

Industry/Entity Type

Technology Equipment

Font styles to use
Other font styles liked:
• Cisco Sans

Colors
33a6d7
cfdeed
85acd3
85cae6
fcf7c1
3377b5
fee18a

Requirements
Must have
• Consistent theme
Professional almost marketing look and feel
Nice to have
• none
Should not have
• none

```html
<!DOCTYPE html>
<html lang="en">
<head>
<meta charset="utf-8">
<title>Future POV – Motsavin</title>
<link href="https://fonts.googleapis.com/css2?family=Barlow:wght@400;500;600;700&display=swap" rel="stylesheet">
<style>
:root{
  --ink:#000;
  --royal:#1d5fbd;
  --royal-deep:#0f4c9e;
  --navy-text:#1c4f9c;
  --sky:#33a6d7;
  --sky-soft:#85cae6;
  --steel:#85acd3;
  --ocean:#3377b5;
  --mist:#cfdeed;
  --paper:#f4f6fa;
  --white:#fff;
  --alert:#c8202a;
}
*{box-sizing:border-box;margin:0;padding:0}
html,body{width:1200px;height:1054px;overflow:hidden;background:var(--ink)}
body{position:relative;font-family:'Barlow',sans-serif;color:var(--white)}
.slide{position:absolute;overflow:hidden}
.abs{position:absolute}

/* title */
.title-slide{left:18px;top:16px;width:570px;height:324px;background:var(--royal)}
.title-slide .backdrop{inset:0;background:linear-gradient(135deg,#2a6cc8 0%,#1a56b0 55%,#2463bd 100%)}
.title-slide .owner{left:0;right:0;top:166px;text-align:center;line-height:20px}
.owner .name{font-weight:700;font-size:19px}
.owner .date{font-size:18px}
.title-card{left:90px;top:230px;width:404px;height:94px;background:var(--paper);border-radius:8px 8px 0 0;text-align:center;color:var(--navy-text)}
.title-card .role{font-weight:700;font-size:28px;margin-top:16px;letter-spacing:.5px}
.title-card .doc{font-size:22px;margin-top:2px}

/* theme */
.theme-slide{left:608px;top:16px;width:574px;height:326px;background:var(--royal)}
.theme-slide .art{left:0;top:0;width:574px;height:210px;background:radial-gradient(ellipse at 55% 45%,rgba(15,70,160,.55),rgba(29,95,189,0) 70%)}
.theme-slide .ghost{left:10px;top:248px;font-size:84px;font-weight:700;color:rgba(255,255,255,.07);letter-spacing:2px;white-space:nowrap}
.theme-slide .word{left:20px;top:196px;width:300px;font-size:44px;line-height:48px;font-weight:700;letter-spacing:0;white-space:nowrap}
.theme-slide .blurb{left:342px;top:174px;width:210px;font-size:8.6px;line-height:12.8px;text-align:justify;hyphens:auto}
.page-tag{left:534px;top:309px;width:24px;height:17px;background:var(--alert);font-size:8px;font-weight:600;text-align:center;line-height:17px}

/* contents */
.toc-slide{left:18px;top:358px;width:574px;height:326px;background:#1a56ad}
.toc-slide .art{inset:0;background:linear-gradient(120deg,#2060b8,#1a52a6)}
.toc-slide .heading{left:75px;top:144px;font-size:20px;font-weight:700}
.toc-list{left:313px;top:28px;width:261px;height:286px;background:#0f4fa6;border-radius:10px 0 0 10px;list-style:none;padding:50px 0 0 34px}
.toc-list li{height:38.4px;font-size:15px}
.toc-list b{display:inline-block;width:29px;font-weight:700}

/* success */
.success-slide{left:608px;top:360px;width:574px;height:326px;background:var(--paper)}
.success-slide .bar{left:2px;top:9px;width:5px;height:24px;background:var(--royal)}
.success-slide h2{position:absolute;left:14px;top:5px;font-size:26px;font-weight:700;color:var(--navy-text)}
.success-slide .intro{left:20px;right:20px;top:55px;font-size:12.5px;line-height:19.2px;text-align:center;color:#3b6fc4}
.goals{left:0;top:126px;width:574px;height:200px;display:flex}
.goal{height:100%;text-align:center;padding-top:26px;font-size:15px;line-height:20.5px}
.goal svg{display:block;margin:0 auto 14px;width:50px;height:50px}
.g1{width:120px;background:var(--royal-deep)}
.g2{width:116px;background:#2f9dd6}
.g3{width:113px;background:var(--sky-soft);color:#eef8fc}
.g4{width:113px;background:var(--steel)}
.g5{width:112px;background:var(--ocean)}

/* values */
.values-slide{left:16px;top:706px;width:574px;height:328px;background:var(--white)}
.photo{background:linear-gradient(160deg,#8d8f94,#3a3d44)}
.p1{left:0;top:0;width:390px;height:196px}
.p2{left:5px;top:202px;width:192px;height:120px;background:linear-gradient(160deg,#d8d6d2,#8b3a34)}
.p3{left:397px;top:4px;width:172px;height:160px;background:linear-gradient(180deg,#a9aeb6,#2c2f35)}
.p4{left:397px;top:170px;width:172px;height:152px;background:linear-gradient(160deg,#5b5d62,#1e1f23)}
.p1 .venue{position:absolute;right:40px;top:22px;font-size:18px;font-weight:600;color:#2b2b2b;letter-spacing:1px}
.values-box{left:202px;top:146px;width:188px;height:182px;background:var(--royal);text-align:center}
.values-box::before{content:"";position:absolute;left:-9px;top:22px;border:9px solid transparent;border-left:0;border-right-color:var(--royal)}
.values-box h3{font-size:28px;font-weight:700;line-height:30px;margin-top:13px}
.values-box p{font-size:15.5px;line-height:20.5px;margin-top:5px}

/* leadership */
.lead-slide{left:610px;top:709px;width:572px;height:327px;background:var(--paper)}
.lead-slide .bar{left:2px;top:10px;width:5px;height:22px;background:var(--royal)}
.lead-slide h2{position:absolute;left:14px;top:8px;font-size:22px;font-weight:700;color:var(--navy-text)}
.lead-slide .formula{left:10px;top:58px;font-size:15px;color:var(--royal)}
.checks{left:22px;top:84px;list-style:none;font-size:9.8px;color:#333;line-height:19.2px}
.checks li::before{content:"";display:inline-block;width:6px;height:3px;border-left:1.6px solid var(--royal);border-bottom:1.6px solid var(--royal);transform:rotate(-45deg);margin:0 6px 3px 0}
.quote{left:14px;top:180px;width:222px;font-size:13px;line-height:19.5px;text-align:center;color:var(--royal);hyphens:auto}
.quote .text{position:relative;z-index:1}
.quote .mark{position:absolute;font-size:74px;color:#e1e5ec;font-family:Georgia,serif;line-height:1;z-index:0}
.cite{left:14px;top:266px;width:222px;text-align:center;font-size:12.5px;font-weight:700;line-height:18px;color:var(--royal)}
.chess{left:242px;top:0;width:330px;height:219px;background:linear-gradient(150deg,#3e5f95 0%,#1d3766 50%,#d6dbe2 100%)}
.caps{left:242px;top:219px;width:330px;height:108px;background:var(--royal)}
.caps h4{position:absolute;left:8px;top:8px;font-size:17.5px;font-weight:500}
.cap{position:absolute;top:40px;width:90px;margin-left:-45px;text-align:center;font-size:13px}
.cap i{display:flex;align-items:center;justify-content:center;width:38px;height:38px;border-radius:50%;background:var(--sky);margin:0 auto 7px}
</style>
</head>
<body>

<section class="slide title-slide">
  <div class="abs backdrop" role="img" aria-label="Blue-tinted city skyline and blueprint backdrop"></div>
  <div class="abs owner"><div class="name">MOTSAVIN</div><div class="date">MONTH 2020</div></div>
  <div class="abs title-card"><div class="role">NEW ROLE</div><div class="doc">POINT OF VIEW DOCUMENT</div></div>
</section>

<section class="slide theme-slide">
  <div class="abs art" role="img" aria-label="Two hands connecting electric plugs with sparks, blue duotone"></div>
  <div class="abs ghost">ADAPTABILITY</div>
  <div class="abs word">ADAPTABILITY</div>
  <p class="abs blurb" lang="en">Liquorice chupa chups applicake apple pie cupcake brownie bear claw cake gingerbread cotton candy. Bear claw croissant apple pie. Croissant cake sweet puff oreo. Liquorice chupa chups applicake apple pie cupcake brownie bear claw cake gingerbread cotton candy.</p>
  <div class="abs page-tag">01</div>
</section>

<section class="slide toc-slide">
  <div class="abs art" role="img" aria-label="Blue-tinted notebook with handwritten planning notes"></div>
  <div class="abs heading">TABLE OF CONTENTS</div>
  <ol class="abs toc-list">
    <li><b>01</b>About Me</li>
    <li><b>02</b>Leadership Philosophy</li>
    <li><b>03</b>Qualifications</li>
    <li><b>04</b>30-60-90 Day Plan</li>
    <li><b>05</b>FY19 Success Defined</li>
    <li><b>06</b>Sponsors</li>
  </ol>
</section>

<section class="slide success-slide">
  <div class="abs bar"></div>
  <h2>FY – Define Success</h2>
  <p class="abs intro">Liquorice chupa chups applicake apple pie cupcake brownie bear claw cake gingerbread cotton candy. Bear claw croissant apple pie. Croissant cake sweet puff oreo . Liquorice chupa chups applicake apple pie cupcake brownie bear claw cake gingerbread cotton candy.</p>
  <div class="abs goals">
    <div class="goal g1"><svg viewBox="0 0 50 50" fill="none" stroke="#fff" stroke-width="2"><circle cx="25" cy="25" r="20"/><circle cx="25" cy="25" r="12"/><circle cx="25" cy="25" r="4"/><path d="M25 1v14M25 35v14M1 25h14M35 25h14"/></svg>Hit<br>Growth<br>Targets</div>
    <div class="goal g2"><svg viewBox="0 0 50 50" fill="none" stroke="#fff" stroke-width="2.4"><rect x="5" y="8" width="40" height="34"/><path d="M10 36l10-11 7 6 12-13M33 18h6v6"/></svg>Exceed<br>Margin<br>Guidance</div>
    <div class="goal g3"><svg viewBox="0 0 50 50" fill="none" stroke="#fff" stroke-width="2"><circle cx="25" cy="25" r="21"/><circle cx="25" cy="25" r="3"/><path d="M25 25l8-10M25 8v4M9 25h4M37 25h4M13 13l3 3M37 13l-3 3"/></svg>Consistency in<br>Execution &amp;<br>Brilliant in the<br>Basics</div>
    <div class="goal g4"><svg viewBox="0 0 50 50" fill="none" stroke="#fff" stroke-width="2.2"><rect x="19" y="5" width="12" height="12"/><rect x="5" y="33" width="12" height="12"/><rect x="33" y="33" width="12" height="12"/><path d="M25 17v8H11v8M25 25h14v8M5 11h9M41 11h-9"/></svg>Executive<br>Relevance</div>
    <div class="goal g5"><svg viewBox="0 0 50 50" fill="none" stroke="#fff" stroke-width="2.2"><rect x="4" y="6" width="28" height="22"/><rect x="14" y="16" width="28" height="22"/><circle cx="25" cy="30" r="7"/><path d="M30 35l7 7M38 40h8v6h-8z"/></svg>Vision and<br>Plan set for<br>Next Fiscal</div>
  </div>
</section>

<section class="slide values-slide">
  <div class="abs photo p1" role="img" aria-label="Team group photo at a community food bank volunteer day"><span class="venue">HARVEST SHARE</span></div>
  <div class="abs photo p2" role="img" aria-label="Volunteers in white protective suits in front of a brick wall mural"></div>
  <div class="abs photo p3" role="img" aria-label="Group of colleagues in winter coats on a city street"></div>
  <div class="abs photo p4" role="img" aria-label="Team member singing on stage at an event venue"></div>
  <div class="abs values-box">
    <h3>MY WHAT<br>MATTERS?</h3>
    <p>Servant Leadership<br><b>“Why We CAN”</b> Mindset<br>Culture by Design<br>Golden Rule Be Present</p>
  </div>
</section>

<section class="slide lead-slide">
  <div class="abs bar"></div>
  <h2>Leadership Philosophy</h2>
  <div class="abs formula">My formula for success has been:</div>
  <ul class="abs checks">
    <li>Hiring great leaders</li>
    <li>Over communicating the stretch vision</li>
    <li>Making good, data-driven decisions</li>
    <li>Finding ways to scale it</li>
  </ul>
  <div class="abs quote" lang="en"><span class="mark" style="left:-6px;top:-22px">“</span><span class="mark" style="right:-8px;top:52px">”</span><span class="text">Great leaders are almost always great simplifiers, who can cut through argument, debate and doubt to offer a solution everybody can understand.</span></div>
  <div class="abs cite">– Gen. Alan Mercer,<br>former U.S. Secretary of State</div>
  <div class="abs chess" role="img" aria-label="Hand moving a chess piece on a board, blue toned"></div>
  <div class="abs caps">
    <h4>Key Capabilities</h4>
    <div class="cap" style="left:54px"><i><svg width="22" height="22" viewBox="0 0 22 22" fill="none" stroke="#fff" stroke-width="1.6"><circle cx="11" cy="11" r="4"/><path d="M11 2v4M11 16v4M2 11h4M16 11h4M5 5l2 2M15 15l2 2"/></svg></i>Sense-making</div>
    <div class="cap" style="left:138px"><i><svg width="22" height="22" viewBox="0 0 22 22" fill="none" stroke="#fff" stroke-width="1.6"><path d="M11 3l8 15H3z"/><circle cx="11" cy="12" r="2"/></svg></i>Relating</div>
    <div class="cap" style="left:212px"><i><svg width="22" height="22" viewBox="0 0 22 22" fill="none" stroke="#fff" stroke-width="1.6"><circle cx="11" cy="11" r="8"/><circle cx="11" cy="11" r="3"/><path d="M11 1v5M11 16v5M1 11h5M16 11h5"/></svg></i>Visioning</div>
    <div class="cap" style="left:293px"><i><svg width="22" height="22" viewBox="0 0 22 22" fill="#fff"><rect x="3" y="7" width="16" height="11" rx="1.5"/><rect x="8" y="4" width="6" height="4" fill="none" stroke="#fff" stroke-width="1.6"/></svg></i>Inventing</div>
  </div>
</section>

</body>
</html>
```